Zine template for Velvet Orchard Zine

I wanted to create a zine template in inDesign or but could use some design expertise.  I have attached my draft doc.  the zine will sometimes be 32 pages, or 40 pages (8.5inches x 11, folded in 1/2). the publicaton is photocopied so placing pages in right order is important for easier assembly. I can attach sample.
I am open to masthead improvement (velvet orchard...pages you can touch).  But needs to look more like "hand made" -not too slick.  I am open to changing icon (pen dipping in water making waves...) to something that suggests a tactile, sensory impact.
I will fill in content myself for each edition.  But need page set ups that is column grid based.  So I can play with layout.  But wanted  a core based design that can make sure each edition is coherent.
Title page-same format but of course different theme, main pic, and contents
Letter from Editor/Table of Contents-again, format same, but content will change
Need 1 double page layout with double column layout option
1 double page layout with single column layout option
Maybe one with triple column layout option.
Common page number format-using shoe icon
I like idea of common theme based header or footer on each page
Add bus card info under Brindlewick press
Needs to have at least 1/2 inch margin around edges as it is copied and don't want content to bleed off page.
REmember pages stapled so need enough space between columns in middle to allow for staple and still read content
DOes this make sense?  Essentially looking for a mag layout for zine (which is just using std letter size paper, folder, and stapled to make a zine (like a pamphlet).  I uploaded a few samples of layouts and how the pages work.
Let me know if you have questions!

```html
<!DOCTYPE html>
<html lang="en">
<head>
<meta charset="utf-8">
<title>Velvet Orchard Zine · From the Editor</title>
<link rel="stylesheet" href="https://fonts.googleapis.com/css2?family=Arvo:wght@400;700&family=Black+Ops+One&family=Source+Sans+3:ital,wght@0,400;0,700;1,400;1,700&display=swap">
<style>
  :root {
    --ink: #111111;
    --paper: #ffffff;
    --rule: #1a1a1a;
    --photo-light: #bdbdbd;
    --photo-dark: #4a4a4a;
  }
  * { box-sizing: border-box; margin: 0; padding: 0; }
  html, body { width: 776px; height: 1200px; overflow: hidden; background: var(--paper); }
  .page {
    position: relative; width: 776px; height: 1200px;
    color: var(--ink); font-family: "Source Sans 3", Arial, sans-serif;
  }
  .editor-photo {
    position: absolute; left: 80px; top: 82px; width: 166px; height: 170px;
    background: linear-gradient(150deg, var(--photo-light), #8a8a8a 55%, var(--photo-dark));
    border: 2px solid var(--ink);
  }
  .section-tag {
    position: absolute; left: 249px; top: 82px; width: 466px; height: 33px;
    background: var(--ink); color: var(--paper);
    font-family: "Black Ops One", Impact, sans-serif; font-size: 24px; letter-spacing: 1px;
    display: flex; align-items: center; justify-content: center;
  }
  .headline {
    position: absolute; left: 268px; top: 140px; width: 460px;
    font-family: "Arvo", Georgia, serif; font-weight: 700; font-size: 37px; line-height: 38px;
    text-transform: uppercase; letter-spacing: 1.2px; white-space: nowrap;
  }
  .body-copy {
    position: absolute; top: 292px; font-size: 20px; line-height: 22.2px;
  }
  .col-left { left: 80px; width: 313px; }
  .col-right { left: 414px; width: 302px; }
  .body-copy p + p { text-indent: 26px; }
  .drop-cap {
    float: left; font-family: "Arvo", Georgia, serif; font-weight: 700;
    font-size: 64px; line-height: 56px; margin: 2px 6px 0 0;
  }
  .signature { margin-top: 42px; text-align: right; line-height: 22px; }
  .signature .name { font-weight: 700; text-transform: uppercase; font-size: 18px; }
  .signature .role { font-style: italic; font-size: 18px; }
  .contents {
    position: absolute; left: 414px; top: 504px; width: 302px; height: 546px;
    border: 2px solid var(--ink); display: flex; flex-direction: column;
  }
  .contents-title {
    background: var(--ink); color: var(--paper); height: 36px; flex: none;
    font-family: "Black Ops One", Impact, sans-serif; font-size: 24px; letter-spacing: 1px;
    display: flex; align-items: center; padding-left: 10px;
  }
  .contents-list {
    list-style: none; padding: 2px 10px 2px 10px; flex: 1;
    display: flex; flex-direction: column; justify-content: space-between;
  }
  .contents-list li {
    border-bottom: 1px solid var(--rule);
    font-family: "Arvo", Georgia, serif; font-weight: 700; font-size: 13px; line-height: 15px;
    padding: 4px 0 4px;
  }
  .contents-list li:last-child { border-bottom: none; }
  .entry-row { display: flex; align-items: baseline; }
  .entry-row .leader { flex: 1; border-bottom: 2px dotted var(--ink); margin: 0 4px; transform: translateY(-3px); }
  .entry-row .num { min-width: 18px; text-align: right; }
  .shoe-icon {
    position: absolute; left: 82px; top: 1014px; width: 40px; height: 48px;
    background: linear-gradient(180deg, #333, #000);
    clip-path: polygon(0 100%, 0 70%, 55% 60%, 85% 0, 100% 5%, 75% 70%, 100% 100%);
  }
  .page-number {
    position: absolute; left: 80px; top: 1064px; width: 32px; height: 28px;
    background: var(--ink); color: var(--paper);
    font-family: "Arvo", Georgia, serif; font-weight: 700; font-size: 21px;
    display: flex; align-items: center; justify-content: center;
  }
  .footer-rule { position: absolute; left: 80px; right: 61px; top: 1092px; border-top: 2px solid var(--ink); }
  .folio {
    position: absolute; left: 122px; top: 1066px; font-size: 19px; white-space: nowrap;
  }
  .folio em { font-size: 14.5px; font-weight: 700; }
</style>
</head>
<body>
<div class="page">
  <div class="editor-photo" role="img" aria-label="Portrait photo of the editor"></div>
  <div class="section-tag">FROM EDITOR</div>
  <h1 class="headline">Obitio ius, quam<br>quam, quossus,<br>offic tem nestrum</h1>

  <div class="body-copy col-left">
    <p><span class="drop-cap">A</span>borae custruptate volupta ipsaped quatendam, senda et re volum et fuga. Rupiet iusdaeres aliberum idignitat.</p>
    <p>Pellamus aut et am fuga. Ibus dolo beroraepro tem. Ullest explab il iusam utem quatempos explab ium, ulla sequis ea sunt adipsan delicide solore voluptio. Et aut restotas reprae. Saperumenis sit evel ipicaborepd quam faceperum re, qui audi blabora turibusae officimi, core aditaquid eati ut audae pror apidit aut eribus aditibusda vid quiduci cum, omnimos ut ut volum hic temost, occullu ptassitaqui comnimpore natem volora suntis deliquo tecus ut et optiunt.</p>
    <p>Tem que ne ditincipsae audi sin rem fugitae et od minctur, omni odi auda pe cum vel imus sunt.</p>
    <p>Ur sequaep elentur accabo. Solorporit ipsuntu riorit volorepel moditatatur? Quiaerum faciet landuci aut exceatur?Hent</p>
  </div>

  <div class="body-copy col-right">
    <p>electent aborepuditae lici aut labo. Nam dem delenim aionsedit qui il ius exceper essimil il modi adit qui sequos id quis sed ut as re volo</p>
    <div class="signature">
      <div class="name">Maren Holloway-Steed</div>
      <div class="role">Zine Creator, Publisher</div>
    </div>
  </div>

  <section class="contents">
    <h2 class="contents-title">TABLE OF CONTENTS</h2>
    <ol class="contents-list">
      <li><div class="entry-row"><span>Pellamus aut et am fuga</span><span class="leader"></span><span class="num">3</span></div></li>
      <li>Tem que ne ditincipsae<div class="entry-row"><span>audi sin rem</span><span class="leader"></span><span class="num">5</span></div></li>
      <li><div class="entry-row"><span>Ur sequaep elentur accabo</span><span class="leader"></span><span class="num">6</span></div></li>
      <li><div class="entry-row"><span>Pellamus aut et am fuga</span><span class="leader"></span><span class="num">8</span></div></li>
      <li>Tem que ne ditincipsae<div class="entry-row"><span>audi sin rem</span><span class="leader"></span><span class="num">10</span></div></li>
      <li><div class="entry-row"><span>Ur sequaep elentur accabo</span><span class="leader"></span><span class="num">12</span></div></li>
      <li><div class="entry-row"><span>Pellamus aut et am fuga</span><span class="leader"></span><span class="num">13</span></div></li>
      <li>Tem que ne ditincipsae<div class="entry-row"><span>audi sin rem</span><span class="leader"></span><span class="num">15</span></div></li>
      <li><div class="entry-row"><span>Ur sequaep elentur accabo</span><span class="leader"></span><span class="num">16</span></div></li>
      <li><div class="entry-row"><span>Pellamus aut et am fuga</span><span class="leader"></span><span class="num">18</span></div></li>
      <li>Tem que ne ditincipsae<div class="entry-row"><span>audi sin rem</span><span class="leader"></span><span class="num">22</span></div></li>
      <li><div class="entry-row"><span>Ur sequaep elentur accabo</span><span class="leader"></span><span class="num">24</span></div></li>
      <li><div class="entry-row"><span>Pellamus aut et am fuga</span><span class="leader"></span><span class="num">25</span></div></li>
      <li>Tem que ne ditincipsae<div class="entry-row"><span>audi sin rem</span><span class="leader"></span><span class="num">30</span></div></li>
      <li><div class="entry-row"><span>Ur sequaep elentur accabo</span><span class="leader"></span><span class="num">32</span></div></li>
    </ol>
  </section>

  <div class="shoe-icon" role="img" aria-label="High-heel shoe page-number icon"></div>
  <div class="page-number">2</div>
  <div class="footer-rule"></div>
  <div class="folio">volume 2 / 2014 / <em>Have something to say? Contact us at: feedback@velvetorchard.com</em></div>
</div>
</body>
</html>
```